Apartment Investor Business Card Design

Need a new business card designed for my multifamily investment company

Industry/Entity Type

Real Estate

Contact Information for Business Card

Garrick Pelham - President & CEO
Brightwold Holdings, LLC
4838 North 92nd Avenue, Ste 500
Omaha, NE 68999
(402) 555-0147
Garrick@brightwoldholdings.example
Www.BrightwoldHoldings.example

Colors
3176b5

```html
<!DOCTYPE html>
<html lang="en">
<head>
<meta charset="utf-8">
<title>Brightwold Holdings – Business Card</title>
<link href="https://fonts.googleapis.com/css2?family=Cinzel:wght@400;500&family=EB+Garamond:wght@400;600&display=swap" rel="stylesheet">
<style>
  :root {
    --brand-blue: #3176b5;
    --card-dark: #2b2b2b;
    --card-light: #ffffff;
    --ink: #2e2e2e;
    --ink-soft: #555555;
    --on-dark: #f2f2f2;
    --stage: #e6e6e6;
  }
  * { margin: 0; padding: 0; box-sizing: border-box; }
  html, body { width: 1200px; height: 900px; overflow: hidden; }
  body {
    background: var(--stage);
    position: relative;
    font-family: "EB Garamond", Georgia, serif;
  }
  .card {
    position: absolute;
    width: 700px;
    height: 400px;
    border-radius: 4px;
    box-shadow: 0 10px 30px rgba(0,0,0,0.18);
    overflow: hidden;
  }
  .card--back {
    left: 90px; top: 40px;
    background: var(--card-dark);
    display: flex; flex-direction: column;
    align-items: center; justify-content: center;
  }
  .card--front {
    left: 410px; top: 470px;
    background: var(--card-light);
  }
  .brand {
    display: flex; align-items: center; gap: 14px;
    font-family: "Cinzel", "Times New Roman", serif;
    font-weight: 400;
    letter-spacing: 0.04em;
  }
  .brand__dot {
    width: 22px; height: 22px; border-radius: 50%;
    background: var(--brand-blue);
    flex: none;
  }
  .card--back .brand__name { color: var(--on-dark); font-size: 42px; }
  .website {
    margin-top: 46px;
    font-family: "EB Garamond", Georgia, serif;
    font-size: 15px;
    font-weight: 600;
    letter-spacing: 0.22em;
    color: var(--on-dark);
  }
  .website__domain { color: var(--brand-blue); }

  .card--front .brand {
    position: absolute; right: 40px; top: 60px;
    gap: 10px;
  }
  .card--front .brand__dot { width: 14px; height: 14px; }
  .card--front .brand__name { color: var(--ink); font-size: 24px; }

  .skyline {
    position: absolute; left: 0; bottom: 0;
    width: 700px; height: 400px;
  }
  .contact {
    position: absolute; left: 40px; top: 140px;
    z-index: 1;
    color: var(--ink);
    line-height: 1.25;
  }
  .contact__name { color: var(--brand-blue); font-weight: 600; font-size: 21px; }
  .contact__title { font-size: 15px; margin-bottom: 16px; }
  .contact__line {
    display: flex; align-items: center; gap: 8px;
    font-size: 15px;
  }
  .contact__line svg { width: 14px; height: 14px; fill: var(--brand-blue); flex: none; }
  .contact__company {
    margin-top: 6px;
    font-family: "Cinzel", "Times New Roman", serif;
    color: var(--brand-blue); font-size: 17px;
  }
  .contact__address { font-size: 15px; color: var(--ink-soft); }
</style>
</head>
<body>

  <section class="card card--back" aria-label="Card back">
    <div class="brand">
      <span class="brand__dot"></span>
      <span class="brand__name">BRIGHTWOLD HOLDINGS</span>
    </div>
    <p class="website">www.<span class="website__domain">BrightwoldHoldings.example</span></p>
  </section>

  <section class="card card--front" aria-label="Card front">
    <div class="brand">
      <span class="brand__dot"></span>
      <span class="brand__name">BRIGHTWOLD HOLDINGS</span>
    </div>

    <svg class="skyline" viewBox="0 0 700 400" role="img" aria-label="City skyline silhouette rising across the bottom of the card">
      <polygon points="0,372 700,250 700,400 0,400" fill="var(--brand-blue)"/>
    </svg>

    <div class="contact">
      <p class="contact__name">Garrick Pelham</p>
      <p class="contact__title">President &amp; CEO</p>
      <p class="contact__line">
        <svg viewBox="0 0 24 24" aria-hidden="true"><path d="M6.6 10.8a15.1 15.1 0 0 0 6.6 6.6l2.2-2.2c.3-.3.7-.4 1-.2 1.1.4 2.3.6 3.6.6.6 0 1 .4 1 1V20c0 .6-.4 1-1 1C10.6 21 3 13.4 3 4c0-.6.4-1 1-1h3.5c.6 0 1 .4 1 1 0 1.3.2 2.5.6 3.6.1.3 0 .7-.2 1z"/></svg>
        (402) 555-0147
      </p>
      <p class="contact__line">
        <svg viewBox="0 0 24 24" aria-hidden="true"><path d="M2 5h20v14H2z M2 5l10 8 10-8" fill="var(--brand-blue)" stroke="#fff" stroke-width="1.5"/></svg>
        Garrick@brightwoldholdings.example
      </p>
      <p class="contact__company">BRIGHTWOLD HOLDINGS, LLC</p>
      <p class="contact__address">4838 North 92nd Avenue, Ste 500 Omaha, NE 68999</p>
    </div>
  </section>

</body>
</html>
```